Real Estate Open House A Frame Sign

The sign is 22" wide and 28" tall. This sign is used to post around the neighbourhood to direct people to an open house (home that is for sale). It is also used for self-promotion.

Designwise
- I just want something with a modern look, simple and clean.
- I want my picture and business logo on the left side.
- On the right side, website (www.lumen-homefinder.com) and my phone (555-347-9182), then a blank space where I can write an address when I need to.

I'm not sure how I want the overall design look. I'm very open-minded and I'm depending on your creative mind to come up with something.

If you have any questions, please let me know.

```html
<!DOCTYPE html>
<html lang="en">
<head>
<meta charset="utf-8">
<title>Open House A-Frame Sign – Lumen Homefinder</title>
<link rel="stylesheet" href="https://fonts.googleapis.com/css2?family=Michroma&display=swap">
<style>
  :root {
    --navy: #004080;
    --logo-navy: #003d7a;
    --paper: #ffffff;
    --ink: #111111;
    --blue-bright: #0a6fe0;
    --blue-deep: #0a4da6;
    --headline: #0b5fc8;
    --photo-light: #e9ebee;
    --photo-dark: #2c323b;
  }
  html, body {
    margin: 0;
    padding: 0;
    width: 1200px;
    height: 761px;
    overflow: hidden;
    background: var(--paper);
  }
  .canvas {
    position: relative;
    width: 1200px;
    height: 761px;
  }
  .sign {
    position: absolute;
    top: 4px;
    width: 591px;
    height: 752px;
    font-family: "Michroma", "Arial", sans-serif;
  }
  .sign--left  { left: 4px; }
  .sign--right { left: 605px; }
  .sign__frame  { fill: var(--navy); }
  .sign__panel  { fill: var(--paper); }
  .logo__box    { fill: var(--logo-navy); }
  .logo__name   { fill: var(--paper); }
  .headline     { fill: var(--headline); }
  .arrow        { fill: var(--paper); }
  .contact      { fill: var(--ink); }
</style>
</head>
<body>
<main class="canvas">

  <!-- Sign face: arrow pointing left -->
  <svg class="sign sign--left" viewBox="0 0 660 840" xmlns="http://www.w3.org/2000/svg">
    <defs>
      <linearGradient id="photoToneL" x1="0" y1="0" x2="0" y2="1">
        <stop offset="0" stop-color="var(--photo-light)"/>
        <stop offset="0.35" stop-color="#8a8f97"/>
        <stop offset="1" stop-color="var(--photo-dark)"/>
      </linearGradient>
      <linearGradient id="bandToneL" x1="0" y1="0" x2="1" y2="0">
        <stop offset="0" stop-color="var(--blue-deep)"/>
        <stop offset="0.6" stop-color="var(--blue-bright)"/>
        <stop offset="1" stop-color="var(--blue-deep)"/>
      </linearGradient>
      <filter id="headlineShadowL" x="-5%" y="-20%" width="110%" height="150%">
        <feDropShadow dx="1" dy="4" stdDeviation="2" flood-color="#000" flood-opacity="0.35"/>
      </filter>
    </defs>
    <rect class="sign__frame" x="0" y="0" width="660" height="840"/>
    <rect class="sign__panel" x="20" y="22" width="620" height="798"/>

    <rect class="agent-photo" role="img" aria-label="Portrait photo of the agent in a dark suit, arms crossed"
          x="30" y="35" width="275" height="415" fill="url(#photoToneL)"/>

    <g class="logo">
      <rect class="logo__box" x="320" y="57" width="305" height="138"/>
      <text class="logo__name" x="472" y="130" text-anchor="middle" font-size="48" textLength="250" lengthAdjust="spacingAndGlyphs">LUMEN</text>
      <text class="logo__name" x="472" y="172" text-anchor="middle" font-size="19" textLength="250" lengthAdjust="spacing">HOMEFINDER</text>
    </g>

    <g class="headline" filter="url(#headlineShadowL)">
      <text x="295" y="330" font-size="66" textLength="330" lengthAdjust="spacingAndGlyphs">OPEN</text>
      <text x="200" y="410" font-size="66" textLength="425" lengthAdjust="spacingAndGlyphs">HOUSE</text>
    </g>

    <path d="M5,470 Q327,432 650,470 L650,612 Q327,652 5,612 Z" fill="#000" opacity="0.25"/>
    <path class="band" d="M5,457 Q327,420 650,457 L650,600 Q327,640 5,600 Z" fill="url(#bandToneL)"/>
    <path class="arrow" d="M135,530 L285,462 L285,500 L525,500 L525,555 L285,555 L285,595 Z"/>

    <text class="contact contact--phone" x="335" y="685" text-anchor="middle" font-size="44" textLength="470" lengthAdjust="spacing">555.347.9182</text>
    <text class="contact contact--web" x="335" y="740" text-anchor="middle" font-size="20" textLength="507" lengthAdjust="spacing">WWW.LUMEN-HOMEFINDER.COM</text>
    <text class="contact contact--address" x="330" y="795" text-anchor="middle" font-size="15" textLength="128" lengthAdjust="spacing">ADDRESS</text>
  </svg>

  <!-- Sign face: arrow pointing right -->
  <svg class="sign sign--right" viewBox="0 0 660 840" xmlns="http://www.w3.org/2000/svg">
    <defs>
      <linearGradient id="photoToneR" x1="0" y1="0" x2="0" y2="1">
        <stop offset="0" stop-color="var(--photo-light)"/>
        <stop offset="0.35" stop-color="#8a8f97"/>
        <stop offset="1" stop-color="var(--photo-dark)"/>
      </linearGradient>
      <linearGradient id="bandToneR" x1="0" y1="0" x2="1" y2="0">
        <stop offset="0" stop-color="var(--blue-deep)"/>
        <stop offset="0.6" stop-color="var(--blue-bright)"/>
        <stop offset="1" stop-color="var(--blue-deep)"/>
      </linearGradient>
      <filter id="headlineShadowR" x="-5%" y="-20%" width="110%" height="150%">
        <feDropShadow dx="1" dy="4" stdDeviation="2" flood-color="#000" flood-opacity="0.35"/>
      </filter>
    </defs>
    <rect class="sign__frame" x="0" y="0" width="660" height="840"/>
    <rect class="sign__panel" x="20" y="22" width="620" height="798"/>

    <rect class="agent-photo" role="img" aria-label="Portrait photo of the agent in a dark suit, arms crossed"
          x="30" y="35" width="275" height="415" fill="url(#photoToneR)"/>

    <g class="logo">
      <rect class="logo__box" x="320" y="57" width="305" height="138"/>
      <text class="logo__name" x="472" y="130" text-anchor="middle" font-size="48" textLength="250" lengthAdjust="spacingAndGlyphs">LUMEN</text>
      <text class="logo__name" x="472" y="172" text-anchor="middle" font-size="19" textLength="250" lengthAdjust="spacing">HOMEFINDER</text>
    </g>

    <g class="headline" filter="url(#headlineShadowR)">
      <text x="295" y="330" font-size="66" textLength="330" lengthAdjust="spacingAndGlyphs">OPEN</text>
      <text x="200" y="410" font-size="66" textLength="425" lengthAdjust="spacingAndGlyphs">HOUSE</text>
    </g>

    <path d="M5,470 Q327,432 650,470 L650,612 Q327,652 5,612 Z" fill="#000" opacity="0.25"/>
    <path class="band" d="M5,457 Q327,420 650,457 L650,600 Q327,640 5,600 Z" fill="url(#bandToneR)"/>
    <path class="arrow" d="M525,530 L375,462 L375,500 L135,500 L135,555 L375,555 L375,595 Z"/>

    <text class="contact contact--phone" x="335" y="685" text-anchor="middle" font-size="44" textLength="470" lengthAdjust="spacing">555.347.9182</text>
    <text class="contact contact--web" x="335" y="740" text-anchor="middle" font-size="20" textLength="507" lengthAdjust="spacing">WWW.LUMEN-HOMEFINDER.COM</text>
    <text class="contact contact--address" x="330" y="795" text-anchor="middle" font-size="15" textLength="128" lengthAdjust="spacing">ADDRESS</text>
  </svg>

</main>
</body>
</html>
```